Business Card, A4 Letter Head and DL Envelope for Vantrelle

We are looking for a design for our Business Card, A4 Letter Head and DL Envelope.

Vantrelle is a distributor of promotional products. We specialize in a range of branded promotional products, these include pens, polo shirts, key rings, drink bottles, uniforms and bags to name a few. We are experts in marketing and assist companies in choosing the right promotional product for their needs. We will predominately be an online business where customers visit our website and browse our range of promotional products and branding options.

Our colours are black, red, white and grey.

Files must be supplied in eps, pdf and ai format.

Please display the following information:
Corbin Hale
Account Manager
Suite xxx, 214 Dawlish Parade Melbourne, Victoria 3000
Phone +61 3 5550 1827
Mobile +61 455 501 936
sales@vantrelle.com.au
www.vantrelle.com.au

```html
<!DOCTYPE html>
<html lang="en">
<head>
<meta charset="utf-8">
<title>Vantrelle – Business Card</title>
<link rel="stylesheet" href="https://fonts.googleapis.com/css2?family=Arimo:wght@400;700&display=swap">
<style>
  :root {
    --canvas: #e4e2df;
    --card-white: #ffffff;
    --ink: #2e2e2e;
    --ink-soft: #8f8f8f;
    --charcoal: #2b2b2b;
    --red: #d71920;
    --grey-dark: #8a8a8a;
    --grey-mid: #b4b4b4;
    --grey-light: #e2e2e2;
    --back-base: #f3f3f3;
  }
  html, body {
    margin: 0;
    width: 1200px;
    height: 900px;
    overflow: hidden;
    background: var(--canvas);
    font-family: "Arimo", Arial, sans-serif;
  }
  .sheet {
    position: relative;
    width: 1200px;
    height: 900px;
  }
  .card {
    position: absolute;
    left: 280px;
    width: 640px;
    height: 366px;
    overflow: hidden;
    box-shadow: 0 6px 18px rgba(0,0,0,.18);
  }
  .card--back { top: 54px; background: var(--back-base); }
  .card--front { top: 480px; background: var(--card-white); }
  .card svg.card__art {
    position: absolute;
    inset: 0;
    width: 100%;
    height: 100%;
  }
  .brand {
    position: absolute;
    display: flex;
    align-items: center;
    color: var(--ink);
    font-weight: 700;
    letter-spacing: .5px;
    text-transform: uppercase;
  }
  .brand__dot {
    border-radius: 50%;
    background: var(--red);
    flex: none;
  }
  .card--front .brand { left: 232px; top: 64px; font-size: 30px; gap: 14px; }
  .card--front .brand__dot { width: 46px; height: 46px; }
  .card--back .brand { left: 262px; top: 118px; font-size: 42px; gap: 18px; }
  .card--back .brand__dot { width: 84px; height: 84px; }
  .back__web {
    position: absolute;
    left: 364px;
    top: 182px;
    font-size: 16px;
    color: var(--ink);
  }
  .contact {
    position: absolute;
    left: 62px;
    top: 176px;
    color: var(--ink);
    line-height: 1.22;
  }
  .contact__name { font-size: 20px; }
  .contact__role { font-size: 18px; font-weight: 700; }
  .contact__mobile { font-size: 18px; }
  .contact__abn { font-size: 15px; color: var(--ink-soft); margin-top: 2px; }
  .address {
    position: absolute;
    left: 62px;
    right: 40px;
    top: 290px;
    color: var(--ink);
    font-size: 16px;
    line-height: 1.5;
  }
  .address__row { display: flex; justify-content: space-between; }
</style>
</head>
<body>
<main class="sheet">

  <section class="card card--back" aria-label="Business card back">
    <svg class="card__art" viewBox="0 0 640 366" aria-hidden="true">
      <path d="M0 0 H220 C180 120 120 250 40 366 H0 Z" fill="var(--grey-dark)"/>
      <path d="M220 0 H270 C230 120 170 250 95 366 H40 C120 250 180 120 220 0 Z" fill="var(--red)"/>
      <path d="M270 0 H300 C260 120 200 250 130 366 H95 C170 250 230 120 270 0 Z" fill="var(--grey-mid)"/>
      <path d="M380 0 H640 V16 C560 24 470 22 380 0 Z" fill="var(--grey-dark)"/>
      <path d="M640 222 V366 H460 C540 330 600 290 640 222 Z" fill="var(--charcoal)"/>
    </svg>
    <div class="brand"><span class="brand__dot"></span><span class="brand__name">Vantrelle</span></div>
    <div class="back__web">www.vantrelle.com.au</div>
  </section>

  <section class="card card--front" aria-label="Business card front">
    <svg class="card__art" viewBox="0 0 640 366" aria-hidden="true">
      <defs>
        <linearGradient id="footerGrey" x1="0" y1="0" x2="0" y2="1">
          <stop offset="0" stop-color="#c9c9c9"/>
          <stop offset="1" stop-color="#a3a3a3"/>
        </linearGradient>
      </defs>
      <path d="M0 0 H300 C210 40 110 62 0 72 Z" fill="var(--charcoal)"/>
      <path d="M0 76 C110 66 210 44 310 0" fill="none" stroke="var(--red)" stroke-width="4"/>
      <path d="M0 262 C220 236 450 208 640 150 V175 C450 232 220 258 0 285 Z" fill="var(--grey-light)"/>
      <path d="M0 366 V285 C220 258 450 232 640 175 V366 Z" fill="url(#footerGrey)"/>
    </svg>
    <div class="brand"><span class="brand__dot"></span><span class="brand__name">Vantrelle</span></div>
    <div class="contact">
      <div class="contact__name">Corbin Hale</div>
      <div class="contact__role">Account Manager</div>
      <div class="contact__mobile">M: +61 455 501 936</div>
      <div class="contact__abn">ABN&nbsp; 00 000 000 000</div>
    </div>
    <div class="address">
      <div class="address__line">Suite xxx, 214 Dawlish Parade Melbourne, Victoria 3000</div>
      <div class="address__row"><span>T: +61 3 5550 1827</span><span>E: sales@vantrelle.com.au</span></div>
    </div>
  </section>

</main>
</body>
</html>
```